Banner Ad Design for Resume Builder Needed

For the ad copy and design of the ad, I leave that up to you. Keep in mind this is a do-it-yourself online resume builder. The site is simple to use and geared towards people who are unsure of how to write/create their own resume.

You can view the site (which isn't finished) and how it works at http://cvcrafter.demo.tplwerks.net/

I do not want the same color scheme or the logo used in the ad, just the most appealing ad for those looking to use a product like this

I need the ad in these sizes:

300x250, 728x90, 160x600, 468x60, 120x600, 300x100

```html
<!DOCTYPE html>
<html lang="en">
<head>
<meta charset="utf-8">
<title>CV Crafter – Banner Ad Set</title>
<link rel="stylesheet" href="https://fonts.googleapis.com/css2?family=Raleway:wght@300;400;700;800&family=Arimo:wght@400&display=swap">
<style>
  :root{
    --brown:#9b4b33;
    --brown-dark:#7d3a26;
    --blue:#1b98e0;
    --paper:#ffffff;
    --frame:#3a3a3a;
    --ink:#333333;
    --wood:#8a4519;
    --wood-light:#c27a45;
    --sheet:#eeebe7;
  }
  html,body{margin:0;padding:0;width:1200px;height:1199px;overflow:hidden;background:var(--paper);}
  .stage{position:relative;width:1254px;height:1253px;transform:scale(0.95694);transform-origin:0 0;
    font-family:'Raleway',sans-serif;color:var(--brown);}
  .sheet-frame{position:absolute;inset:0;border:1.5px solid #666;box-sizing:border-box;}
  .size-label{position:absolute;font-family:'Arimo',sans-serif;font-size:48px;color:var(--ink);line-height:1;}
  .banner{position:absolute;overflow:hidden;box-sizing:border-box;background:var(--paper);}
  .framed{border:2px solid var(--frame);}
  .banner > *{position:absolute;margin:0;}
  .banner p{white-space:nowrap;}
  .photo{background:linear-gradient(125deg,var(--wood) 0%,var(--wood-light) 30%,var(--sheet) 55%,#f7f5f2 80%,#d9cfc5 100%);}
  .photo-fade{background:linear-gradient(90deg,rgba(255,255,255,1) 0%,rgba(255,255,255,0) 35%),linear-gradient(125deg,var(--wood-light),var(--sheet) 50%,#f3f0ec);}
  .light{font-weight:300;}
  .bold{font-weight:800;}
  .t{line-height:1;}
  .url{font-family:'Arimo',sans-serif;}
  .btn{background:var(--brown);color:var(--paper);font-weight:300;display:flex;align-items:center;justify-content:center;white-space:nowrap;}
  .btn-line{border:1.5px solid var(--paper);color:var(--paper);font-weight:400;display:flex;align-items:center;justify-content:center;white-space:nowrap;}
  .white{color:var(--paper);}
  .ink{color:var(--ink);}
  .blue{color:var(--blue);}
</style>
</head>
<body>
<div class="stage">
  <div class="sheet-frame"></div>

  <div class="size-label" style="left:358px;top:42px;">468x60</div>
  <div class="size-label" style="left:312px;top:243px;">728x90</div>
  <div class="size-label" style="left:926px;top:167px;">300x250</div>
  <div class="size-label" style="left:167px;top:537px;">160x600</div>
  <div class="size-label" style="left:545px;top:537px;">120x600</div>
  <div class="size-label" style="left:857px;top:855px;">300x100</div>

  <!-- 468x60 A -->
  <div class="banner framed" style="left:207px;top:99px;width:470px;height:61px;">
    <div class="photo-fade" role="img" aria-label="Photo of a hand signing a resume on a clipboard" style="left:250px;top:0;width:220px;height:61px;"></div>
    <p class="t" style="left:18px;top:6px;font-size:11px;">Create a</p>
    <p class="t" style="left:18px;top:21px;font-size:15px;"><span class="bold">PROFESSIONAL RESUME</span> <span style="font-size:11px;">in minutes</span></p>
    <p class="t" style="left:18px;top:40px;font-size:11px;">that will separate you from the competition.</p>
  </div>

  <!-- 468x60 B -->
  <div class="banner framed" style="left:207px;top:171px;width:470px;height:61px;">
    <div class="photo" role="img" aria-label="Photo of a hand signing a resume on a clipboard" style="left:0;top:0;width:80px;height:61px;"></div>
    <p class="t light" style="left:95px;top:22px;font-size:22.5px;">BUILD YOUR</p>
    <p class="t bold" style="left:238px;top:14px;font-size:32px;">RESUME</p>
    <div style="left:393px;top:-3px;width:68px;height:68px;border-radius:50%;background:var(--brown);"></div>
    <p class="white light" style="left:393px;top:6px;width:68px;text-align:center;font-size:21px;line-height:24px;">Learn<br>More</p>
  </div>

  <!-- 728x90 A -->
  <div class="banner" style="left:94px;top:306px;width:728px;height:90px;background:var(--brown);">
    <div role="img" aria-label="Photo of a hand signing a resume on a clipboard" style="left:370px;top:0;width:358px;height:90px;background:linear-gradient(90deg,var(--brown) 0%,rgba(155,75,51,0) 40%),linear-gradient(125deg,var(--wood),var(--sheet) 45%,#f4f1ed 85%,#2a2a2a 100%);"></div>
    <p class="t white" style="left:29px;top:9px;font-size:16px;">Create a</p>
    <p class="t white" style="left:29px;top:31px;font-size:24px;"><span class="bold">PROFESSIONAL RESUME</span> <span style="font-size:16px;">in minutes</span></p>
    <p class="t white" style="left:29px;top:62px;font-size:16px;">that will separate you from the competition.</p>
    <div class="btn" style="left:592px;top:30px;width:120px;height:31px;font-size:19px;">Learn More</div>
  </div>

  <!-- 728x90 B -->
  <div class="banner framed" style="left:94px;top:427px;width:729px;height:90px;">
    <div class="photo" role="img" aria-label="Photo of a hand signing a resume on a clipboard" style="left:0;top:0;width:280px;height:90px;"></div>
    <svg style="left:235px;top:0;" width="50" height="90" viewBox="0 0 50 90"><polygon points="0,0 12,0 48,45 12,90 0,90 36,45" fill="#9b4b33"/><polygon points="12,0 50,0 50,90 12,90 48,45" fill="#fff"/></svg>
    <p class="t" style="left:285px;top:6px;width:315px;text-align:center;font-size:18px;">Create a</p>
    <p class="t bold" style="left:285px;top:36px;width:315px;text-align:center;font-size:24.5px;">PROFESSIONAL RESUME</p>
    <p class="t" style="left:270px;top:68px;width:345px;text-align:center;font-size:12px;">in minutes, that will separate you from the competition.</p>
    <div class="btn" style="left:607px;top:28px;width:118px;height:32px;font-size:20px;">Learn More</div>
  </div>

  <!-- 300x250 A -->
  <div class="banner" style="left:873px;top:245px;width:301px;height:251px;border:2px solid var(--brown);">
    <div class="photo" role="img" aria-label="Photo of a hand signing a resume on a clipboard" style="left:150px;top:0;width:151px;height:251px;"></div>
    <svg style="left:0;top:0;" width="200" height="251" viewBox="0 0 200 251"><polygon points="0,0 188,0 148,185 190,251 0,251" fill="#fff"/><polygon points="176,0 188,0 160,190 190,251 178,251 146,190" fill="#9b4b33"/><polygon points="0,0 145,0 135,55 0,55" fill="#9b4b33"/></svg>
    <p class="white bold" style="left:13px;top:11px;font-size:15px;line-height:16px;">Your Logo<br>Goes Here</p>
    <p class="t" style="left:8px;top:67px;font-size:13px;">Create a</p>
    <p class="bold" style="left:8px;top:84px;font-size:18.5px;line-height:25px;">PROFESSIONAL<br>RESUME</p>
    <p style="left:8px;top:134px;font-size:13px;line-height:16.5px;">in minutes<br>that will separate you<br>from the competition</p>
    <div class="btn" style="left:14px;top:192px;width:120px;height:32px;font-size:20px;">Learn More</div>
  </div>

  <!-- 300x250 B -->
  <div class="banner framed" style="left:870px;top:527px;width:302px;height:250px;">
    <div class="photo" role="img" aria-label="Photo of a hand signing a resume on a clipboard" style="left:0;top:0;width:302px;height:160px;"></div>
    <svg style="left:118px;top:158px;" width="184" height="92" viewBox="0 0 184 92"><polygon points="24,0 184,0 184,92 24,92 24,58 0,48 24,38" fill="#1b98e0"/></svg>
    <p class="t ink" style="left:8px;top:165px;font-size:10px;">Create a</p>
    <p class="blue bold" style="left:8px;top:178px;font-size:14px;line-height:20px;">PROFESSIONAL<br>RESUME <span class="ink" style="font-weight:400;font-size:9.5px;">in minutes</span></p>
    <p class="ink" style="left:8px;top:216px;font-size:9.5px;line-height:12px;">that will separate you<br>from the competition</p>
    <p class="t white light" style="left:150px;top:168px;font-size:24px;">BUILD YOUR</p>
    <p class="t white bold" style="left:149px;top:194px;font-size:33px;">RESUME</p>
    <p class="t white url" style="left:127px;top:234px;font-size:9px;">http://cvcrafter.demo.tplwerks.net/</p>
  </div>

  <!-- 160x600 A -->
  <div class="banner framed" style="left:94px;top:594px;width:161px;height:600px;">
    <div class="photo" role="img" aria-label="Photo of a hand signing a resume on a clipboard" style="left:0;top:0;width:161px;height:270px;"></div>
    <svg style="left:0;top:225px;" width="161" height="60" viewBox="0 0 161 60"><polygon points="0,40 110,0 161,35 161,60 0,60" fill="#fff"/></svg>
    <div style="left:0;top:588px;width:161px;height:12px;background:var(--brown);"></div>
    <p class="t light" style="left:8px;top:282px;font-size:24.5px;">BUILD YOUR</p>
    <p class="t bold" style="left:8px;top:308px;font-size:33px;">RESUME</p>
    <p class="t ink" style="left:8px;top:356px;font-size:12px;">Create a</p>
    <p class="bold" style="left:8px;top:374px;font-size:14.5px;line-height:23px;">PROFESSIONAL<br>RESUME</p>
    <p class="ink" style="left:8px;top:421px;font-size:12px;line-height:18.5px;">in minutes<br>that will separate you<br>from the competition</p>
    <div style="left:32px;top:489px;width:92px;height:92px;border-radius:50%;border:2px solid var(--brown);box-sizing:border-box;"></div>
    <p class="light" style="left:32px;top:510px;width:92px;text-align:center;font-size:23px;line-height:24px;">Learn<br>More</p>
  </div>

  <!-- 160x600 B -->
  <div class="banner framed" style="left:283px;top:594px;width:161px;height:600px;">
    <div class="photo" role="img" aria-label="Photo of a hand signing a resume on a clipboard" style="left:0;top:276px;width:161px;height:324px;"></div>
    <p class="t light" style="left:8px;top:27px;font-size:24.5px;">BUILD YOUR</p>
    <p class="t bold" style="left:8px;top:53px;font-size:33px;">RESUME</p>
    <p class="t ink" style="left:10px;top:100px;font-size:12px;">Create a</p>
    <p class="bold" style="left:10px;top:118px;font-size:14.5px;line-height:25px;">PROFESSIONAL<br>RESUME <span class="ink" style="font-weight:400;font-size:12px;">in minutes</span></p>
    <p class="ink" style="left:10px;top:166px;font-size:12px;line-height:19px;">that will separate you<br>from the competition</p>
    <div class="btn" style="left:19px;top:215px;width:120px;height:32px;font-size:20px;">Learn More</div>
    <div style="left:0;top:582px;width:161px;height:18px;background:var(--brown);"></div>
    <p class="t white url" style="left:3px;top:586px;font-size:8.5px;">http://cvcrafter.demo.tplwerks.net/</p>
  </div>

  <!-- 120x600 A -->
  <div class="banner framed" style="left:545px;top:594px;width:121px;height:600px;">
    <div class="photo" role="img" aria-label="Photo of a hand signing a resume on a clipboard" style="left:0;top:0;width:121px;height:280px;"></div>
    <svg style="left:0;top:250px;" width="121" height="350" viewBox="0 0 121 350"><path d="M0,18 Q80,-10 110,10 Q121,20 121,40 L121,255 L0,255 Z" fill="#fff"/><path d="M0,300 Q10,260 121,255 L121,350 L0,350 Z" fill="#9b4b33"/><path d="M0,300 Q10,262 121,257" fill="none" stroke="#222" stroke-width="3"/></svg>
    <p class="light" style="left:5px;top:277px;font-size:31px;line-height:36px;">BUILD<br>YOUR</p>
    <p class="t bold" style="left:5px;top:350px;font-size:25.5px;">RESUME</p>
    <p class="t ink" style="left:4px;top:396px;font-size:11px;">Create a</p>
    <p class="t bold" style="left:4px;top:413px;font-size:13px;">PROFESSIONAL</p>
    <p class="t bold" style="left:4px;top:435px;font-size:13px;">RESUME <span class="ink" style="font-weight:400;font-size:10.5px;">in minutes</span></p>
    <p class="ink" style="left:4px;top:454px;font-size:10.5px;line-height:17px;">that will separate you<br>from the competition</p>
    <div class="btn-line" style="left:11px;top:544px;width:96px;height:22px;font-size:12.5px;">Learn More ›</div>
  </div>

  <!-- 120x600 B -->
  <div class="banner framed" style="left:682px;top:594px;width:122px;height:600px;">
    <div class="photo" role="img" aria-label="Photo of a hand signing a resume on a clipboard" style="left:0;top:0;width:122px;height:360px;"></div>
    <svg style="left:0;top:290px;" width="122" height="70" viewBox="0 0 122 70"><polygon points="0,0 122,60 122,70 0,70" fill="#fff"/><polygon points="32,8 92,32 88,42 28,18" fill="#9b4b33"/></svg>
    <div style="left:30px;top:0;width:80px;height:8px;background:var(--brown);"></div>
    <p class="light" style="left:0;top:366px;width:118px;text-align:center;font-size:31px;line-height:45px;">BUILD<br>YOUR</p>
    <p class="t bold" style="left:0;top:457px;width:118px;text-align:center;font-size:26px;">RESUME</p>
    <div style="left:0;top:522px;width:122px;height:78px;background:var(--brown);"></div>
    <div class="btn-line" style="left:11px;top:548px;width:96px;height:22px;font-size:12.5px;">Learn More ›</div>
  </div>

  <!-- 300x100 A -->
  <div class="banner framed" style="left:859px;top:938px;width:301px;height:100px;">
    <div class="photo" role="img" aria-label="Photo of a hand signing a resume on a clipboard" style="left:170px;top:0;width:131px;height:100px;"></div>
    <svg style="left:150px;top:0;" width="60" height="100" viewBox="0 0 60 100"><polygon points="0,0 30,0 50,50 30,100 0,100" fill="#fff"/><polygon points="30,0 36,0 56,50 36,100 30,100 50,50" fill="#9b4b33"/></svg>
    <div style="left:58px;top:0;width:72px;height:4px;background:var(--brown);"></div>
    <div style="left:58px;top:94px;width:72px;height:4px;background:var(--brown);"></div>
    <p class="t light" style="left:31px;top:10px;font-size:21px;">BUILD YOUR</p>
    <p class="t bold" style="left:31px;top:32px;font-size:30px;">RESUME</p>
    <div class="btn" style="left:60px;top:68px;width:66px;height:17px;font-size:10.5px;font-weight:400;">Learn More</div>
  </div>

  <!-- 300x100 B -->
  <div class="banner framed" style="left:859px;top:1088px;width:301px;height:100px;">
    <div role="img" aria-label="Photo of a hand signing a resume on a clipboard" style="left:0;top:0;width:301px;height:100px;background:linear-gradient(90deg,var(--brown-dark) 0%,rgba(125,58,38,0.85) 35%,rgba(125,58,38,0.2) 70%),linear-gradient(125deg,var(--wood),#a07a66 50%,#7a5a4a);"></div>
    <p class="t white light" style="left:16px;top:18px;font-size:26px;">BUILD YOUR</p>
    <p class="t white bold" style="left:16px;top:46px;font-size:36px;">RESUME</p>
    <div class="btn-line" style="left:193px;top:61px;width:95px;height:24px;font-size:13.5px;">Learn More ›</div>
  </div>
</div>
</body>
</html>
```